Tin Lantern

I have written a book which I eventually would like to serve a couple of purposes. The initial purpose was to memorialize life events and lessons from my life to pass on to my grandchildren, in hopes they may learn from the experiences. As I completed the book, I now believe I could remove some of the family specific information as much of the information could be useful to many people.

While I want to book to have a great look for the grandkids, more importantly will be the version that we put on the bookshelf to sell. The cover is obviously the first thing a buyer will see and may or may not peak there interest. I would like to include the attached photo as the cover photo and the title language is also attached. Other than that I am not sure what is the best way to design the cover.

```html
<!DOCTYPE html>
<html lang="en">
<head>
<meta charset="utf-8">
<title>Life – book cover</title>
<link rel="stylesheet" href="https://fonts.googleapis.com/css2?family=Fredoka:wght@500;600;700&display=swap">
<style>
  :root {
    --page-bg: #ffffff;
    --band-black: #000000;
    --band-red: #f0474f;
    --band-grey: #b3b3b3;
    --band-green: #76d17c;
    --band-yellow: #ece713;
    --spine-green: #2fd35a;
    --spine-blue: #2f86d8;
    --spine-cyan: #5ccfd6;
    --spine-pale: #a9e6e4;
    --spine-ink: #2c8a3a;
    --photo-frame: #2fcf5a;
    --ink-white: #ffffff;
    --ink-black: #111111;
    --hi-green: #8fe88c;
    --life-pink: #ec5a92;
    --life-blue: #3aa0e0;
    --life-red: #e83a32;
    --life-yellow: #f3e81c;
  }
  * { box-sizing: border-box; margin: 0; padding: 0; }
  html, body {
    width: 991px; height: 1200px; overflow: hidden;
    background: var(--page-bg);
  }
  .book {
    position: absolute; left: 100px; top: 30px;
    width: 777px; height: 1140px;
    display: flex;
    font-family: "Fredoka", "Arial Rounded MT Bold", sans-serif;
    box-shadow: 0 10px 30px rgba(0,0,0,.18);
  }

  /* Spine */
  .spine {
    position: relative; width: 64px; height: 100%;
    display: flex; flex-direction: column;
    border-right: 2px solid rgba(0,0,0,.15);
  }
  .spine-band { width: 100%; }
  .spine-band--black { height: 80px; background: var(--band-black); }
  .spine-band--red { height: 110px; background: var(--band-red); }
  .spine-band--grey { height: 125px; background: var(--band-grey); }
  .spine-band--green { height: 150px; background: var(--band-green); }
  .spine-band--bright { height: 140px; background: var(--spine-green); }
  .spine-band--blue { height: 140px; background: var(--spine-blue); }
  .spine-band--cyan { height: 140px; background: var(--spine-cyan); }
  .spine-band--pale { height: 140px; background: var(--spine-pale); }
  .spine-band--yellow { height: 115px; background: var(--band-yellow); }
  .spine-title {
    position: absolute; left: 0; top: 96px; width: 64px;
    writing-mode: vertical-rl;
    display: flex; align-items: center;
    font-weight: 600; font-size: 40px; line-height: 64px;
    color: var(--spine-ink); white-space: nowrap;
    text-shadow: 1px 1px 0 rgba(255,255,255,.35);
  }
  .spine-title .dash { margin: 14px 0; color: var(--ink-black); }
  .spine-title .l { color: var(--life-pink); }
  .spine-title .i { color: var(--band-black); }
  .spine-title .f { color: var(--life-red); }
  .spine-title .e { color: var(--life-yellow); text-shadow: 1px 1px 0 rgba(0,0,0,.4); }

  /* Front cover */
  .cover {
    position: relative; width: 713px; height: 100%;
    display: flex; flex-direction: column;
  }
  .band { position: relative; width: 100%; }
  .band--greeting {
    height: 80px; background: var(--band-black);
    display: flex; align-items: center; padding-left: 44px;
  }
  .greeting { color: var(--hi-green); font-weight: 600; font-size: 40px; }
  .band--names { height: 110px; background: var(--band-red); }
  .name {
    position: absolute; color: var(--ink-white); font-weight: 600; font-size: 31px;
    line-height: 1; text-shadow: 1px 2px 2px rgba(0,0,0,.35);
  }
  .band--tagline {
    height: 125px; background: var(--band-grey);
    color: var(--ink-white); font-weight: 600; font-size: 23px;
    text-shadow: 1px 1px 2px rgba(0,0,0,.45);
  }
  .tagline-line { position: absolute; white-space: nowrap; }
  .tagline-line strong { font-size: 31px; font-weight: 700; }
  .band--title {
    height: 150px; background: var(--band-green);
    display: flex; align-items: center; justify-content: center;
  }
  .title {
    font-weight: 700; font-size: 128px; line-height: 1; letter-spacing: 2px;
    text-shadow: 3px 4px 0 rgba(40,40,40,.75);
  }
  .title .l { color: var(--life-pink); }
  .title .i { color: var(--life-blue); }
  .title .f { color: var(--life-red); }
  .title .e { color: var(--life-yellow); }
  .band--photo {
    height: 560px; background: var(--band-green);
    border: 4px solid var(--photo-frame);
  }
  .family-photo {
    width: 100%; height: 100%;
    background: linear-gradient(180deg, #2b2018 0%, #4a3a2c 40%, #6f7f52 75%, #4f6a2f 100%);
  }
  .band--closing {
    height: 115px; background: var(--band-yellow);
    display: flex; align-items: center; padding-left: 32px;
  }
  .closing { color: var(--ink-black); font-weight: 600; font-size: 33px; white-space: nowrap; }
  .closing strong { font-size: 40px; font-weight: 700; }
</style>
</head>
<body>
  <main class="book">
    <aside class="spine">
      <div class="spine-band spine-band--black"></div>
      <div class="spine-band spine-band--red"></div>
      <div class="spine-band spine-band--grey"></div>
      <div class="spine-band spine-band--green"></div>
      <div class="spine-band spine-band--bright"></div>
      <div class="spine-band spine-band--blue"></div>
      <div class="spine-band spine-band--cyan"></div>
      <div class="spine-band spine-band--pale"></div>
      <div class="spine-band spine-band--yellow"></div>
      <p class="spine-title">Tin Lantern<span class="dash">-</span><span class="l">L</span><span class="i">i</span><span class="f">f</span><span class="e">e</span></p>
    </aside>

    <section class="cover">
      <header class="band band--greeting">
        <h2 class="greeting">Hi Guys</h2>
      </header>

      <div class="band band--names">
        <span class="name" style="left:6px; top:58px;">Theo</span>
        <span class="name" style="left:64px; top:24px;">Oliver</span>
        <span class="name" style="left:158px; top:58px;">Miles</span>
        <span class="name" style="left:282px; top:24px;">Luke</span>
        <span class="name" style="left:338px; top:58px;">Samuel</span>
        <span class="name" style="left:448px; top:24px;">Isaac</span>
        <span class="name" style="left:548px; top:60px;">Benjamin</span>
      </div>

      <div class="band band--tagline">
        <p class="tagline-line" style="left:176px; top:18px;">There's a <strong>bump</strong> in the road ahead....</p>
        <p class="tagline-line" style="left:436px; top:78px;">It's called...</p>
      </div>

      <div class="band band--title">
        <h1 class="title"><span class="l">L</span><span class="i">i</span><span class="f">f</span><span class="e">e</span></h1>
      </div>

      <div class="band band--photo">
        <div class="family-photo" role="img" aria-label="Family photo: a grandfather seated on the lawn in front of a porch with his six grandsons gathered around him"></div>
      </div>

      <footer class="band band--closing">
        <p class="closing">This is about having <strong>a great one.</strong></p>
      </footer>
    </section>
  </main>
</body>
</html>
```